Flyer für Personalreferentin
Zielgruppe
Freiberufliche Personalreferentin. Ich unterstütze Unternehmen (zeitweise) in den Personalabteilungen (Rekrutierung, Personalverwaltung, Mitarbeiterbetreuung). Zielgruppe sind Unternehmen, die moderne Personalarbeit abbilden möchten.
Aufgabenstellung
Der Flyer soll 2-seitig sein. Seite 1 - Werbetext und Seite 2 bzw. Rückseite mein Profil bzw. meinen Lebenslauf ansprechend dargestellt. Ich möchte ein modernes, minimalistisches Design.
Ziel wäre einen Flyer zu erhalten, den man an die Unternehmen senden kann um auf die Dienstleistung aufmerksam zu machen. Logo und Profilbild sollen verwendet werden, weitere Bilder gern mitvorschlagen.

```html
<!DOCTYPE html>
<html lang="de">
<head>
<meta charset="utf-8">
<title>Lena Marwitz – HR Freelancer Flyer</title>
<link rel="stylesheet" href="https://fonts.googleapis.com/css2?family=Montserrat:wght@300;400;600;700&family=Source+Sans+3:ital,wght@0,400;0,600;0,700;1,400&display=swap">
<style>
:root{
  --bg:#ebe9ea;
  --paper:#f2f1f1;
  --red:#c5584a;
  --red-text:#cf4d3c;
  --ink:#1e1e1e;
  --body:#3a3a3a;
  --grey-bar:#5b5b5d;
  --white:#ffffff;
}
*{box-sizing:border-box;margin:0;padding:0}
html,body{width:1200px;height:800px;overflow:hidden;background:var(--bg)}
body{position:relative;font-family:"Source Sans 3",Arial,sans-serif;color:var(--body)}
.page{position:absolute;top:30px;width:525px;height:740px;background:var(--paper);overflow:hidden}
.page--front{left:55px}
.page--back{left:620px}
.abs{position:absolute}

/* Front page */
.hero{left:0;top:0;width:525px;height:207px;
  background:linear-gradient(180deg,#d6d8dd 0%,#e3e4e7 55%,#eeeeef 100%)}
.hero__photo{left:0;top:0;width:525px;height:120px;
  background:linear-gradient(90deg,#cfd2d8 0%,#e2e3e6 30%,#d9dbe0 60%,#cdd3dd 100%);opacity:.8}
.brand{left:0;width:525px;top:62px;text-align:center;font-family:"Montserrat",sans-serif;font-weight:300}
.brand__name{font-size:25px;color:#6d6d6d;letter-spacing:.5px}
.brand__role{font-size:11px;color:#4a4a4a;margin-top:4px;letter-spacing:.8px}
.headline{left:82px;width:361px;top:131px;text-align:center;font-family:"Montserrat",sans-serif;
  font-weight:700;font-size:12px;line-height:21px;color:var(--ink);text-transform:uppercase}
.headline em{font-style:normal;color:var(--red-text)}
.intro{left:0;top:207px;width:525px;height:78px;background:var(--red);color:var(--white);
  font-size:8.6px;line-height:16px;text-align:center;padding:15px 40px 0}
.benefits-title{left:60px;top:300px;font-weight:700;font-size:11px;color:var(--red-text)}
.benefit{width:208px;font-size:8.6px;line-height:15.8px;color:var(--body)}
.benefit h3{font-size:9px;font-weight:600;color:var(--red-text);position:relative;line-height:16px}
.benefit h3::before{content:"";position:absolute;left:-11px;top:6px;width:4px;height:4px;border-radius:50%;background:var(--red-text)}
.cta{left:290px;top:611px;width:193px;height:129px;background:var(--red);color:#fbe9e4;
  font-size:8.8px;line-height:16px;padding:33px 18px 0 25px;z-index:2}
.footer-bar{left:0;bottom:0;width:525px;height:24px;background:var(--grey-bar)}

/* Back page */
.portrait{left:49px;top:16px;width:144px;height:156px;border-radius:2px;
  background:radial-gradient(ellipse at 50% 30%,#d8b48f 0%,#b89170 30%,#3b3b3b 75%,#242424 100%)}
.name{left:212px;top:28px;font-family:"Montserrat",sans-serif;font-weight:700;font-size:31px;letter-spacing:.5px;color:var(--ink)}
.name span{color:var(--red-text)}
.tagline{left:213px;top:66px;font-size:14px;color:var(--ink)}
.birth{left:213px;top:101px;font-size:8.6px;color:var(--ink)}
.birth b{font-weight:400;color:var(--red-text)}
.contact{font-size:8.6px;line-height:16px;color:var(--ink);display:flex;gap:6px}
.contact svg{flex:none;margin-top:3px}
.quote{left:0;top:172px;width:525px;height:71px;background:var(--red);color:var(--white)}
.quote__mark{left:46px;top:0;font-family:Georgia,serif;font-size:40px;line-height:60px}
.quote__text{left:81px;top:15px;width:410px;font-size:8.4px;line-height:15px}
.section-title{font-weight:700;font-size:10.5px;color:var(--ink);letter-spacing:.2px}
.section-title span{color:var(--red-text)}
.job{font-size:7.6px;line-height:13px;color:var(--ink)}
.job h4{font-size:7.8px;font-weight:700}
.job .org{color:var(--red-text)}
.job ul{list-style:none;margin-top:3px}
.job li{position:relative;padding-left:9px}
.job li::before{content:"";position:absolute;left:1px;top:5.5px;width:3px;height:3px;border-radius:50%;background:var(--ink)}
.edu-box{left:283px;top:405px;width:225px;height:137px;border:1px solid #7a7a7a;padding:16px 0 0 20px}
.lang-box{left:283px;top:589px;width:225px;height:116px;background:var(--red);color:var(--white);padding:18px 20px 0 20px}
.lang-box .section-title{color:var(--white)}
.lang{position:relative;height:30px;font-size:8px}
.lang__label{position:absolute;left:0;top:0}
.lang__bars{position:absolute;left:42px;top:5px;display:flex;gap:4px}
.lang__bars i{display:block;width:22px;height:2.5px;background:var(--white)}
.lang__level{position:absolute;right:0;top:12px;font-style:italic;font-size:7.8px}
.back-bar{left:0;bottom:0;width:525px;height:13px;background:var(--grey-bar)}
</style>
</head>
<body>

<section class="page page--front">
  <div class="abs hero"></div>
  <div class="abs hero__photo" role="img" aria-label="Aufgehelltes Foto eines Teams im Besprechungsgespräch am Tisch"></div>
  <div class="abs brand">
    <div class="brand__name">lena marwitz</div>
    <div class="brand__role">HR Freelancer</div>
  </div>
  <h1 class="abs headline">Sie suchen einen erfahrenen Personalrefer&shy;enten <em>mit einem modernen Verständnis von Personalarbeit und Mitarbeiterführung?</em></h1>
  <p class="abs intro">Ich biete Ihnen 10 Jahre Berufserfahrung, nachgewiesene Expertise in der Personalentwicklung und Führung, sowie eine empathische, diskrete und zuverlässige Arbeitsweise. Als freiberuflicher Personalreferent stehe ich Ihnen flexibel und bedarfsgerecht zur Verfügung, um Ihr Unternehmen erfolgreich zu unterstützen.</p>
  <h2 class="abs benefits-title">Ein freiberuflicher Personalreferent bietet zudem eine Reihe von Vorteilen:</h2>

  <div class="abs benefit" style="left:60px;top:336px">
    <h3>Flexibilität</h3>
    <p>Als Freiberufler können Personalreferenten flexibel auf die Anforderungen und Bedürfnisse eines Unternehmens reagieren. Sie können sowohl für kurzfristige Projekte als auch für langfristige Engagements engagiert werden, je nach Bedarf des Unternehmens.</p>
  </div>
  <div class="abs benefit" style="left:60px;top:463px">
    <h3>Kostenersparnis</h3>
    <p>Die Beauftragung eines freiberuflichen Personal&shy;referenten kann kostengünstiger sein als die Einstellung eines festangestellten Mitarbeiters. Unternehmen können die Kosten für Sozialleistungen, Lohnnebenkosten und Fortbildungsmaßnahmen einsparen.</p>
  </div>
  <div class="abs benefit" style="left:60px;top:590px">
    <h3>Unabhängigkeit</h3>
    <p>Freiberufliche Personalreferenten arbeiten selbstständig und eigenverantwortlich. Sie bringen frische Perspektiven und neue Ideen in das Unternehmen ein, ohne von internen Strukturen oder Unternehmenskulturen beeinflusst zu sein.</p>
  </div>
  <div class="abs benefit" style="left:291px;top:336px">
    <h3>Fachkenntnisse und Erfahrung</h3>
    <p>Freiberufliche Personalreferenten verfügen in der Regel über umfangreiche Fachkenntnisse und langjährige Erfahrung in verschiedenen Branchen. Sie bringen wertvolles Know-how und Best Practices mit, um effektive HR-Strategien und -Prozesse zu entwickeln und umzusetzen.</p>
  </div>
  <div class="abs benefit" style="left:291px;top:463px">
    <h3>Fachkenntnisse und Erfahrung</h3>
    <p>Freiberufliche Personalreferenten können auf bestimmte HR-Bereiche spezialisiert sein, wie z.B. Rekrutierung, Personalentwicklung oder Arbeitsrecht. Unternehmen können von dieser Spezialisierung profitieren und sich auf Expertenwissen verlassen, um spezifische HR-Herausforderungen anzugehen.</p>
  </div>

  <div class="abs footer-bar"></div>
  <p class="abs cta">Kontaktieren Sie mich jetzt, um zu erfahren, wie ich Ihre HR-Prozesse optimieren und Ihr Team zum Erfolg führen kann.</p>
</section>

<section class="page page--back">
  <div class="abs portrait" role="img" aria-label="Porträtfoto der Personalreferentin mit verschränkten Armen"></div>
  <h1 class="abs name">LENA <span>MARWITZ</span></h1>
  <p class="abs tagline">Freelance Personalbereich</p>
  <p class="abs birth"><b>Geburtsdatum/ -ort:</b> 14.05.1989 in Wittenfeld</p>
  <div class="abs contact" style="left:213px;top:128px">
    <svg width="8" height="10" viewBox="0 0 8 10"><path d="M4 0a4 4 0 0 0-4 4c0 3 4 6 4 6s4-3 4-6a4 4 0 0 0-4-4zm0 5.5a1.5 1.5 0 1 1 0-3 1.5 1.5 0 0 1 0 3z" fill="#cf4d3c"/></svg>
    <div>Lindenweg 21<br>D-14712 Birkenau</div>
  </div>
  <div class="abs contact" style="left:340px;top:128px">
    <svg width="9" height="9" viewBox="0 0 10 10"><path d="M2 .5l2 2-1 1.3c.6 1.3 1.6 2.3 2.9 2.9L7.2 5.7l2 2L8 9.5C4 9.2.8 6 .5 2z" fill="#cf4d3c"/></svg>
    <div>0176 48 15 90 27</div>
  </div>
  <div class="abs contact" style="left:340px;top:144px">
    <svg width="9" height="9" viewBox="0 0 10 10"><rect x="0" y="2" width="10" height="7" fill="#cf4d3c"/><path d="M0 2l5 4 5-4" stroke="#f2f1f1" fill="none"/></svg>
    <div>mail@lenamarwitz.de</div>
  </div>

  <div class="abs quote">
    <div class="abs quote__mark">“</div>
    <p class="abs quote__text">Für die Tätigkeit im Personalwesen bringe ich ein abgeschlossenes Studium im Personalbereich, aufgrund meiner Ausbildung zur Hotelfachfrau den notwendigen Dienstleistungsgedanken sowie umfassende praktische Erfahrungen in verschiedenen Bereichen der Personalarbeit.</p>
  </div>

  <h2 class="abs section-title" style="left:41px;top:265px">BERUFLICHE <span>ERFAHRUNG</span></h2>

  <article class="abs job" style="left:41px;top:292px;width:230px">
    <h4>HR Generalist</h4>
    <p><span class="org">Nordlicht Service GmbH, Berlin</span>&nbsp;&nbsp; 03.2018 - 12.2023</p>
    <ul>
      <li>Personalbetreuung und -verwaltung</li>
      <li>vorbereitende Lohn- und Gehaltsabrechnung</li>
      <li>Durchführung des BEM-Verfahrens</li>
      <li>Rekrutierung</li>
    </ul>
  </article>

  <article class="abs job" style="left:41px;top:392px;width:230px">
    <h4>HR Assistant Manager / Recruitment Manager</h4>
    <p class="org">Modehaus Kerner Ltd. &amp; Co. KG,</p>
    <p><span class="org">Berlin und deutschlandweit</span>&nbsp;&nbsp; 09.2014 – 02.2018</p>
    <ul>
      <li>Personalbetreuung und -verwaltung</li>
      <li>Deutschlandweite Rekrutierung von Mitarbeitern u.a. im Rahmen von Filialeröffnungen</li>
      <li>Durchführen von Bewerbungsinterviews an Standorten</li>
      <li>bundesweit</li>
      <li>Begleitung des kompletten Einstellungsprozesses</li>
      <li>Unterstützung des Führungsteams</li>
      <li>Kontrolle der Gehaltsabrechnung und des Berichtswesen Zusammenarbeit mit der Arbeitnehmervertretung</li>
    </ul>
  </article>

  <article class="abs job" style="left:41px;top:561px;width:230px">
    <h4>HR Coordinator</h4>
    <p><span class="org">Wanderhof Hotel Gruppe, Berlin</span>&nbsp;&nbsp; 08.2013 – 08.2014</p>
    <ul>
      <li>Operative Personalarbeit von Recruiting inkl. Stellenausschrei&shy;bungen, über Vertragsgestaltung, zu Personalbetreuung bis zur Abwicklung aller Formalitäten bei Austritten</li>
      <li>Implementierung und Weiterentwicklung bestehender HR- Prozesse</li>
      <li>Personalverwaltung einzelner Häuser europaweit, inkl. vorbereitende Lohn- und Gehaltsabrechnung</li>
      <li>Präsentation des Unternehmens auf Messen, Schulen etc.</li>
      <li>Mitarbeit an verschiedenen HR-Projekten wie z.B. Einführung eines unternehmensweiten Sprachkurses</li>
    </ul>
  </article>

  <article class="abs job" style="left:303px;top:292px;width:210px">
    <h4>Praktikum in der Personalabteilung</h4>
    <p class="org">Hotel Alpenblick Berlin, Alpenblick Hotels &amp; Resorts</p>
    <p>09.2010 – 02.2011</p>
    <ul>
      <li>Vorbereitung und Abwicklung aller Formalitäten bei der Einstellung neuer Mitarbeiter</li>
      <li>Pflegen der Online-Recruitingportale</li>
      <li>Gestaltung von Stellenanzeigen</li>
    </ul>
  </article>

  <div class="abs edu-box">
    <h2 class="section-title">BERUFSAUS- <span>UND WEITERBILDUNG</span></h2>
    <div class="job" style="margin-top:10px">
      <h4>Studium der Betriebswirtschaftslehre</h4>
      <p><span class="org">Hochschule Spreetal</span>&nbsp;&nbsp; 10.2008 – 03.2012</p>
      <ul style="margin-top:4px">
        <li>Abschluss: Bachelor of Arts (B.A.)</li>
        <li>Schwerpunkt Personal und Organisation</li>
      </ul>
      <h4 style="margin-top:8px">Ausbildung zur Hotelfachfrau</h4>
      <p><span class="org">Hotel Elbterrasse Wittenfeld</span>&nbsp;&nbsp; 08.2006 - 07.2008</p>
    </div>
  </div>

  <div class="abs lang-box">
    <h2 class="section-title" style="margin-bottom:14px">BERUFSAUS- UND WEITERBILDUNG</h2>
    <div class="lang">
      <span class="lang__label">Englisch</span>
      <span class="lang__bars"><i></i><i></i><i></i><i></i><i></i></span>
      <span class="lang__level">verhandlungssicher</span>
    </div>
    <div class="lang">
      <span class="lang__label">Spanisch</span>
      <span class="lang__bars"><i></i><i></i></span>
      <span class="lang__level">Grundkenntnisse</span>
    </div>
  </div>

  <div class="abs back-bar"></div>
</section>

</body>
</html>
```